Tambrel Couriers Web design

Take a look at our existing website(www.tmbrl-example.com) and design a new one, plus coding and recreate an existing logo.

```html
<!DOCTYPE html>
<html lang="en">
<head>
<meta charset="UTF-8">
<title>Tambrel Couriers</title>
<link href="https://fonts.googleapis.com/css2?family=Poppins:wght@300;400;500;600;700&display=swap" rel="stylesheet">
<style>
:root{
  --blue:#0b4f9c;
  --ink:#1c1c1f;
  --muted:#5b5f66;
  --soft:#eef4fd;
  --grey:#f5f5f6;
  --footer:#121214;
  --stage:#e9ecf1;
  --line:#c9ccd2;
}
*{margin:0;padding:0;box-sizing:border-box}
html,body{width:1200px;height:3546px;overflow:hidden}
body{background:var(--stage);font-family:'Poppins',sans-serif;color:var(--ink);position:relative}
.page{position:absolute;left:245px;top:0;width:710px;height:3546px;background:#fff;overflow:hidden}
section,header,footer{position:absolute;left:0;width:710px}
.abs{position:absolute}
.btn{position:absolute;background:var(--blue);color:#fff;font-size:8px;display:flex;align-items:center;justify-content:center;gap:10px;border-radius:1px}
.title{position:absolute;left:0;width:710px;text-align:center;font-size:17px;font-weight:600}
.title span{border-bottom:2px solid var(--blue);padding-bottom:1px}
.sub{position:absolute;left:0;width:710px;text-align:center;font-size:7px;color:var(--muted)}
.para{font-size:7.4px;line-height:15px;color:var(--muted)}
.photo{position:absolute;border-radius:2px}
/* nav */
.nav{top:0;height:37px;background:#fff}
.brand{position:absolute;left:54px;top:10px;display:flex;align-items:center;gap:5px;font-size:7.5px;font-weight:600;color:var(--blue)}
.brand i{width:12px;height:12px;background:var(--blue);display:block;border-radius:2px}
.menu{position:absolute;right:54px;top:14px;display:flex;gap:14px;font-size:8px}
.menu .on{color:var(--blue);position:relative}
.menu .on:after{content:"";position:absolute;left:-6px;right:-6px;top:22px;height:2px;background:var(--blue)}
/* hero */
.hero{top:37px;height:362px;background:linear-gradient(100deg,#5c5148 0%,#7b6b5c 35%,#b0552f 60%,#6e5a48 85%,#4a4038 100%)}
.hero .t1{left:54px;top:36px;color:#fff;font-size:20px;font-weight:300}
.hero .t2{left:54px;top:66px;color:#fff;font-size:22px;font-weight:700;line-height:31px}
.hero .t2 u{text-decoration:none;border-bottom:2px solid #fff}
.hero .p{left:54px;top:162px;width:235px;color:#fff;font-size:7.4px;line-height:13px}
/* about */
.about{top:399px;height:367px}
/* benefits */
.benefits{top:766px;height:401px;background:var(--soft)}
.benefit{position:absolute;top:156px;width:130px;text-align:center}
.benefit .ic{width:52px;height:48px;margin:0 auto;border-radius:6px;background:linear-gradient(135deg,#9db6d8,#2d4f86)}
.benefit h4{font-size:8.5px;font-weight:500;margin-top:22px;line-height:13px}
.benefit p{font-size:6.6px;color:var(--muted);line-height:11px;margin-top:6px}
/* services */
.svc{height:auto}
.svc h3{position:absolute;font-size:12px;font-weight:600;line-height:18px}
/* logistics */
.logi{top:2009px;height:457px}
.item{position:absolute;width:176px;text-align:center}
.item svg{display:block;margin:0 auto}
.item h4{font-size:8.5px;font-weight:500;line-height:13px;margin-top:14px}
.item p{font-size:6.6px;color:var(--muted);line-height:11px;margin-top:6px}
.card{position:absolute;background:#fff;box-shadow:0 2px 10px rgba(0,0,0,.08)}
/* testimonial */
.testi{top:2466px;height:355px;background:var(--soft)}
.tcard{position:absolute;background:#fff;box-shadow:0 2px 8px rgba(0,0,0,.06);text-align:center}
.tcard .av{width:26px;height:26px;border-radius:50%;margin:14px auto 0;background:linear-gradient(135deg,#8a6a58,#3a2e28)}
.tcard p{font-size:6px;color:var(--muted);line-height:9.5px;padding:0 14px;margin-top:12px}
.tcard h5{font-size:8px;font-weight:500;margin-top:12px}
.tcard small{display:block;font-size:6.5px;color:#9a9ea5;margin-top:4px}
.tcard .foot{position:absolute;left:14px;right:14px;bottom:12px;display:flex;justify-content:space-between;align-items:center;font-size:6px;color:var(--muted)}
.tcard .foot a{color:var(--muted);text-decoration:underline}
.dots{display:flex;gap:4px}
.dots i{width:7px;height:7px;border:1px solid var(--muted);border-radius:50%;display:block}
/* contact */
.contact{top:2821px;height:516px}
.form{position:absolute;left:356px;top:125px;width:300px;height:317px;background:var(--grey)}
.field{position:absolute;background:#fff;border:1px solid var(--line);border-radius:3px;font-size:6.5px;color:#9a9ea5;padding:6px 14px}
/* footer */
.footer{top:3337px;height:209px;background:var(--footer);color:#fff}
.footer .col{position:absolute;font-size:6.5px}
.footer .links div{height:19px}
.footer .social{display:flex;gap:8px}
.footer .social i{width:9px;height:9px;border:1px solid #fff;border-radius:50%;display:block}
.footer .row{display:flex;gap:8px;align-items:flex-start;height:19px}
</style>
</head>
<body>
<div class="page">

<header class="nav">
  <div class="brand"><i></i>Tambrel Couriers</div>
  <nav class="menu">
    <span class="on">Home</span><span>About</span><span>Services ▾</span><span>Customer Benefits ▾</span><span>Logistics ▾</span><span>Contact</span>
  </nav>
</header>

<section class="hero" role="img" aria-label="Photo of a smiling courier in a red cap greeting a customer at a doorway">
  <div class="abs t1">We are here</div>
  <div class="abs t2">What Kind of <u>Services</u><br>Do you want</div>
  <p class="abs p">Lorem Ipsum is simply dummy text of the printing and typesetting industry. Lorem Ipsum has been the industry's standard dummy text ever since the 1500s.</p>
  <div class="btn" style="left:54px;top:219px;width:92px;height:29px">Contact us <span>›</span></div>
</section>

<section class="about">
  <div class="title" style="top:40px"><span>About us</span></div>
  <div class="sub" style="top:82px">Lorem Ipsum is simply dummy text of the printing and</div>
  <h2 class="abs" style="left:70px;top:140px;font-size:17.5px;font-weight:600;line-height:24px;width:290px">As a professional why should you choose us?</h2>
  <p class="abs para" style="left:70px;top:203px;width:248px">Lorem Ipsum is simply dummy text of the printing and typesetting industry. Lorem Ipsum has been the industry's standard dummy text ever since the 1500s, when an unknown printer took a galley of type and scrambled it to make a type specimen book. It has survive not only five centuries.</p>
  <div class="btn" style="left:70px;top:304px;width:85px;height:28px">View more</div>
  <div class="photo" style="left:406px;top:132px;width:250px;height:172px;background:linear-gradient(120deg,#3b3f45,#c33a2c 45%,#c9a27a 75%,#8c7358)" role="img" aria-label="Photo of a masked courier checking a tablet beside parcels in a van"></div>
</section>

<section class="benefits">
  <div class="title" style="top:44px"><span>Customer&nbsp; Benefits</span></div>
  <div class="sub" style="top:86px">Lorem Ipsum is simply dummy text of the printing and</div>
  <div class="benefit" style="left:56px"><div class="ic" role="img" aria-label="Illustration of a warehouse"></div><h4>Free waiting<br>time</h4><p>Lorem Ipsum is simply dummy text of the printing and typesetting industry</p></div>
  <div class="benefit" style="left:206px"><div class="ic" role="img" aria-label="Illustration of a service box"></div><h4>All our services are<br>guaranteed</h4><p>Lorem Ipsum is simply dummy text of the printing and typesetting industry</p></div>
  <div class="benefit" style="left:364px"><div class="ic" role="img" aria-label="Illustration of a delivery truck"></div><h4>Pickup within 15 to 30 mins<br>of your call or sooner</h4><p>Lorem Ipsum is simply dummy text of the printing and typesetting industry</p></div>
  <div class="benefit" style="left:521px"><div class="ic" role="img" aria-label="Illustration of parcels and a location pin"></div><h4>First 100lbs.<br>are free</h4><p>Lorem Ipsum is simply dummy text of the printing and typesetting industry</p></div>
  <div class="btn" style="left:311px;top:321px;width:85px;height:28px">View all</div>
</section>

<section class="svc" style="top:1167px;height:347px">
  <div class="title" style="top:34px"><span>Our Services</span></div>
  <div class="sub" style="top:76px">Lorem Ipsum is simply dummy text of the printing and</div>
  <div class="photo" style="left:54px;top:137px;width:250px;height:171px;background:linear-gradient(180deg,#f1f1f0,#dcdcda 60%,#a89a86)" role="img" aria-label="Photo of a courier holding a box in front of a white van"></div>
  <h3 style="left:398px;top:138px;width:265px">Hospital &amp; Medical Care – Home Deliveries, Pharmaceuticals and Critical Routes.</h3>
  <p class="abs para" style="left:398px;top:186px;width:250px">Lorem Ipsum is simply dummy text of the printing and typesetting industry. Lorem Ipsum has been the industry's standard dummy text ever since the 1500s, when an unknown printer took a</p>
  <div class="btn" style="left:398px;top:242px;width:85px;height:28px">View more</div>
</section>

<section class="svc" style="top:1514px;height:231px;background:var(--grey)">
  <h3 style="left:54px;top:31px;width:290px">Banking &amp; Brokerage – Emergency Deliveries, Mortgage Documents, Interoffice Routes.</h3>
  <p class="abs para" style="left:54px;top:78px;width:250px">Lorem Ipsum is simply dummy text of the printing and typesetting industry. Lorem Ipsum has been the industry's standard dummy text ever since the 1500s, when an unknown printer took a</p>
  <div class="btn" style="left:54px;top:137px;width:85px;height:28px">View more</div>
  <div class="photo" style="left:406px;top:30px;width:250px;height:171px;background:linear-gradient(110deg,#1e4ea8,#2b5fbf 40%,#c49a70 60%,#6d8a5c)" role="img" aria-label="Photo of a courier handing a parcel to a customer paying by card"></div>
</section>

<section class="svc" style="top:1745px;height:264px">
  <div class="photo" style="left:54px;top:40px;width:250px;height:170px;background:linear-gradient(135deg,#1c1e22,#3a3d44 50%,#b8b2a8)" role="img" aria-label="Photo of a hand stamping a legal document"></div>
  <h3 style="left:413px;top:40px;width:250px">Legal, Administrative and also deliveries associated with Manufacturing.</h3>
  <p class="abs para" style="left:413px;top:88px;width:250px">Lorem Ipsum is simply dummy text of the printing and typesetting industry. Lorem Ipsum has been the industry's standard dummy text ever since the 1500s, when an unknown printer took a</p>
  <div class="btn" style="left:413px;top:146px;width:85px;height:28px">View more</div>
</section>

<section class="logi">
  <div class="title" style="top:24px"><span>Logistics</span></div>
  <div class="sub" style="top:66px">Lorem Ipsum is simply dummy text of the printing and</div>
  <div class="card" style="left:267px;top:118px;width:176px;height:138px"></div>
  <div class="item" style="left:81px;top:135px">
    <svg width="34" height="26" viewBox="0 0 34 26" fill="none" stroke="#1c1c1f" stroke-width="1.4"><rect x="2" y="3" width="18" height="15"/><path d="M20 8h6l5 5v5H20z"/><circle cx="8" cy="21" r="3"/><circle cx="26" cy="21" r="3"/></svg>
    <h4>Expert in Logistics<br>Transportation</h4><p>Lorem Ipsum is simply dummy text<br>of the printing and typesetting industry.<br>Lorem Ipsum has been the industry's</p></div>
  <div class="item" style="left:267px;top:135px">
    <svg width="34" height="26" viewBox="0 0 34 26" fill="none" stroke="#1c1c1f" stroke-width="1.4"><rect x="11" y="2" width="14" height="11"/><path d="M15 2v5h6V2"/><path d="M2 16h8l6 3h10l6-4M2 22h22l8-7"/></svg>
    <h4>US DOT &amp; NY DOT<br>Authority</h4><p>Lorem Ipsum is simply dummy text<br>of the printing and typesetting industry.<br>Lorem Ipsum has been the industry's</p></div>
  <div class="item" style="left:456px;top:135px">
    <svg width="34" height="26" viewBox="0 0 34 26" fill="none" stroke="#1c1c1f" stroke-width="1.4"><rect x="8" y="3" width="14" height="14"/><path d="M22 8h5l5 5v4H22z"/><path d="M2 7h4M1 11h5M3 15h3"/><circle cx="13" cy="20" r="3"/><circle cx="27" cy="20" r="3"/></svg>
    <h4>Lift-gate equipped<br>Trucks</h4><p>Lorem Ipsum is simply dummy text<br>of the printing and typesetting industry.<br>Lorem Ipsum has been the industry's</p></div>
  <div class="item" style="left:173px;top:289px">
    <svg width="34" height="28" viewBox="0 0 34 28" fill="none" stroke="#1c1c1f" stroke-width="1.4"><path d="M24 2l-10 20"/><circle cx="12" cy="24" r="3"/><rect x="10" y="6" width="10" height="10" transform="rotate(25 15 11)"/><path d="M24 2h5"/></svg>
    <h4>Warehousing/<br>Distribution</h4><p>Lorem Ipsum is simply dummy text<br>of the printing and typesetting industry.<br>Lorem Ipsum has been the industry's</p></div>
  <div class="item" style="left:362px;top:289px">
    <svg width="34" height="28" viewBox="0 0 34 28" fill="none" stroke="#1c1c1f" stroke-width="1.4"><path d="M4 4h22v6H4zM7 10v14M23 10v6"/><circle cx="24" cy="21" r="6"/><path d="M21 21l2 2 4-4"/></svg>
    <h4>Scheduled &amp; Routed<br>Services</h4><p>Lorem Ipsum is simply dummy text<br>of the printing and typesetting industry.<br>Lorem Ipsum has been the industry's</p></div>
</section>

<section class="testi">
  <div class="title" style="top:24px"><span>Testimonial</span></div>
  <div class="sub" style="top:66px">Lorem Ipsum is simply dummy text of the printing and</div>
  <div class="tcard" style="left:103px;top:117px;width:150px;height:176px">
    <div class="av" role="img" aria-label="Portrait photo of a client"></div>
    <p>Lorem Ipsum is simply dummy text of the printing and typesetting industry Lorem Ipsum is simply dummy text of the printing and typesetting industry</p>
    <h5>Lorem Ipsum</h5><small>active</small>
    <div class="foot"><a>Read more</a><div class="dots"><i></i><i></i><i></i></div></div>
  </div>
  <div class="tcard" style="left:272px;top:107px;width:166px;height:195px">
    <div class="av" style="width:30px;height:30px" role="img" aria-label="Portrait photo of a client"></div>
    <p style="font-size:6.8px;line-height:10.5px">Lorem Ipsum is simply dummy text of the printing and typesetting industry Lorem Ipsum is simply dummy text of the printing and typesetting industry</p>
    <h5>Lorem Ipsum</h5><small>active</small>
    <div class="foot"><a>Read more</a><div class="dots"><i></i><i></i><i></i></div></div>
  </div>
  <div class="tcard" style="left:457px;top:117px;width:150px;height:176px">
    <div class="av" role="img" aria-label="Portrait photo of a client"></div>
    <p>Lorem Ipsum is simply dummy text of the printing and typesetting industry Lorem Ipsum is simply dummy text of the printing and typesetting industry</p>
    <h5>Lorem Ipsum</h5><small>active</small>
    <div class="foot"><a>Read more</a><div class="dots"><i></i><i></i><i></i></div></div>
  </div>
  <svg class="abs" style="left:316px;top:326px" width="14" height="8" viewBox="0 0 14 8" fill="none" stroke="#9aa0a8" stroke-width="1"><path d="M13 4H1M4 1L1 4l3 3"/></svg>
  <svg class="abs" style="left:382px;top:326px" width="14" height="8" viewBox="0 0 14 8" fill="none" stroke="#1c1c1f" stroke-width="1"><path d="M1 4h12M10 1l3 3-3 3"/></svg>
</section>

<section class="contact">
  <div class="title" style="top:34px"><span>Contact us</span></div>
  <div class="sub" style="top:76px">Lorem Ipsum is simply dummy text of the printing and</div>
  <h4 class="abs" style="left:54px;top:124px;font-size:8.5px;font-weight:600">As a professional why should you choose us?</h4>
  <p class="abs para" style="left:54px;top:156px;width:205px;line-height:10.5px;font-size:6.8px">Lorem Ipsum is simply dummy text of the printing and typesetting industry. Lorem Ipsum has been the industry's standard dummy text ever since the 1500s, when an unknown printer took a galley of type and scrambled.</p>
  <div class="abs" style="left:61px;top:254px;width:263px;height:159px;background:radial-gradient(ellipse at center,#a8cbe0 0%,#cfe2ee 55%,#fff 80%)" role="img" aria-label="World map with office location pins"></div>
  <div class="form">
    <div class="field" style="left:27px;top:37px;width:245px;height:23px">Full Name</div>
    <div class="field" style="left:27px;top:80px;width:245px;height:23px">City Or Town</div>
    <div class="field" style="left:27px;top:122px;width:118px;height:23px">Email</div>
    <div class="field" style="left:153px;top:122px;width:119px;height:23px">Phone</div>
    <div class="field" style="left:27px;top:164px;width:245px;height:85px;padding-top:10px">Message</div>
    <div class="btn" style="left:27px;top:270px;width:245px;height:22px">Send massage</div>
  </div>
</section>

<footer class="footer">
  <div class="col" style="left:54px;top:36px;width:130px">
    <div style="display:flex;align-items:center;gap:5px;font-size:7.5px;font-weight:600"><i style="width:12px;height:12px;background:#fff;display:block;border-radius:2px"></i>Tambrel Couriers</div>
    <p style="margin-top:14px;line-height:9.5px;font-size:6px">Lorem Ipsum is simply dummy text of the printing and typesetting industry. Lorem Ipsum has been the industry's.</p>
    <div class="social" style="margin-top:12px"><i></i><i></i><i></i><i></i></div>
  </div>
  <div class="col links" style="left:266px;top:38px">
    <div>HOME</div><div>ABOUT US</div><div>SERVICES</div><div>CUSTOMER BENEFITS</div><div>LOGISTICS</div><div>CONTACT US</div>
  </div>
  <div class="col" style="left:387px;top:36px">
    <div class="row"><svg width="9" height="9" viewBox="0 0 10 10" fill="none" stroke="#fff"><path d="M2 1l2 2-1 1.5a6 6 0 003 3L7.5 6l2 2-1.5 1.5C4 9 1 6 .5 2z"/></svg>555-014-2290</div>
    <div class="row"><svg width="9" height="9" viewBox="0 0 10 10" fill="none" stroke="#fff"><rect x=".5" y="1.5" width="9" height="7"/><path d="M.5 1.5l4.5 4 4.5-4"/></svg>info@tmbrl-example.com</div>
    <div class="row" style="line-height:9px"><svg width="9" height="10" viewBox="0 0 10 11" fill="none" stroke="#fff"><path d="M5 10S1 6 1 4a4 4 0 018 0c0 2-4 6-4 6z"/><circle cx="5" cy="4" r="1.4"/></svg>42 HARLOW LANE,<br>FENWICK, NY 10990</div>
  </div>
  <div class="col" style="left:529px;top:38px">
    <div>SUBSCRIBE TO OUR NEWSLETTER</div>
    <div style="margin-top:9px;width:129px;height:23px;border:1px solid #8a8d93;border-radius:2px;padding:6px 10px;color:#b8bbc0">E-mail</div>
    <div style="margin-top:12px;width:73px;height:22px;background:var(--blue);display:flex;align-items:center;justify-content:center;border-radius:1px">Subscribe</div>
  </div>
  <div class="abs" style="left:0;top:169px;width:710px;height:1px;background:#2e2f33"></div>
  <div class="col" style="left:54px;top:183px;font-size:6px">Terms and Conditions &nbsp;&nbsp;&nbsp;&nbsp; Privacy Policy</div>
  <div class="col" style="right:54px;top:183px;font-size:6px">All rights reserved 2021</div>
</footer>

</div>
</body>
</html>
```